Traineeway.Asia, a social enterprise in Asia, needs a website!

I need a website designed for Traineeway.Asia, which is a social enterprise in Asia that connects potential interns with internship opportunities in the region.

Please read the attached wireframe and submit a homepage designs with text, based on the attached wireframe, from which we will choose and select the best design. Please note that we only want website designs; functionality, coding and programming are not required

The designer that provides the best designed home page, will then design all other pages of the website, and will receive the fee. We have already come up with one design (see wireframe in the attached doc) that designers may review for ideas.

University and graduate students in Asia.

Social

5+ page

Sans Serif

• I want a website that doesn't require a significant amount of scrolling, and is well-designed so that it is easy to understand the website's purpose, how to navigate around the website, and utilize it.
• Easy to see all elements of the website without scrolling.

```html
<!DOCTYPE html>
<html lang="en">
<head>
<meta charset="utf-8">
<title>Traineeway.Asia – Home</title>
<link href="https://fonts.googleapis.com/css2?family=Open+Sans:ital,wght@0,400;0,600;0,700;1,400;1,700&display=swap" rel="stylesheet">
<style>
:root{
  --green:#5a9e2a;
  --green-dark:#4a8a1f;
  --ink:#333;
  --muted:#777;
  --line:#ddd;
  --band:#efefef;
  --footer:#1f1f1f;
  --footer-deep:#151515;
  --white:#fff;
}
*{box-sizing:border-box;margin:0;padding:0}
html,body{width:714px;height:1200px;overflow:hidden;background:var(--white)}
body{font-family:"Open Sans",Arial,sans-serif;color:var(--ink);position:relative}
.wrap{position:absolute;left:45px;width:624px}

/* header */
.site-header{position:absolute;top:0;left:0;width:714px;height:52px;background:var(--white)}
.brand{position:absolute;left:45px;top:8px;display:flex;align-items:center;gap:5px;font-weight:700;font-size:15px;color:var(--green)}
.brand .dot{width:12px;height:12px;border-radius:50%;background:var(--green)}
.top-tools{position:absolute;right:45px;top:6px;display:flex;align-items:center;gap:4px;font-size:7px}
.search{color:var(--green);font-weight:600;margin-right:4px}
.search-box{width:70px;height:12px;border:1px solid var(--line)}
.btn-sm{background:var(--green);color:var(--white);padding:2px 9px;font-size:7px}
.main-nav{position:absolute;right:45px;top:33px;display:flex;gap:16px;font-size:7.5px;color:#444}

/* hero */
.hero{position:absolute;top:52px;left:0;width:714px;height:318px;background:linear-gradient(135deg,#e9f1f6 0%,#b9c9a4 35%,#8a7a66 60%,#d7dfe4 100%)}

/* welcome */
.welcome{top:382px}
.section-title{font-style:italic;font-weight:700;color:var(--green);font-size:19px}
.welcome p{font-size:6.5px;line-height:10px;color:var(--muted);margin-top:6px}

/* featured */
.featured{top:488px}
.center-title{text-align:center;font-style:italic;font-weight:700;color:var(--green);font-size:14px;display:flex;align-items:center;gap:10px}
.center-title::before,.center-title::after{content:"";flex:1;border-top:1px solid var(--line)}
.jobs{display:flex;gap:12px;margin-top:10px}
.job{width:147px}
.job .photo{height:78px;background:linear-gradient(135deg,#c9b89e,#7e8f9c)}
.job:nth-child(2) .photo{background:linear-gradient(135deg,#d9cbb6,#8f9a7a)}
.job:nth-child(3) .photo{background:linear-gradient(135deg,#b9c7d2,#9c7f6c)}
.job:nth-child(4) .photo{background:linear-gradient(135deg,#e0d3c2,#6f8570)}
.job p{font-size:6px;line-height:8.5px;color:var(--muted);margin-top:4px}

/* testimonial */
.testimonial{position:absolute;top:645px;left:0;width:714px;height:195px;background:var(--band);text-align:center}
.testimonial h2{font-style:italic;font-weight:400;font-size:19px;color:#444;margin-top:12px}
.quote-mark{display:block;margin:8px auto 0}
.testimonial blockquote{width:520px;margin:10px auto 0;font-style:italic;font-size:7px;line-height:11px;color:var(--muted)}
.testimonial cite{display:block;margin-top:10px;font-size:7px;color:var(--green);font-weight:600;font-style:normal}
.testimonial .role{font-size:6px;color:var(--muted)}

/* resources */
.resources{top:852px;height:140px}
.resources .section-title{font-size:17px;display:flex;align-items:center;gap:10px;width:440px}
.resources .section-title::after{content:"";flex:1;border-top:1px solid var(--line)}
.res-photo{position:absolute;left:0;top:26px;width:130px;height:100px;background:linear-gradient(135deg,#d6c3a8,#8b6f5c 60%,#b6c0c8)}
.res-text{position:absolute;left:143px;top:24px;width:300px;font-size:6.5px;line-height:10px;color:var(--muted)}
.res-text a{color:var(--green);font-weight:600;text-decoration:none}
.newsletter{position:absolute;left:475px;top:18px;width:149px;height:116px;border:1px solid var(--line);background:#f7f7f7}
.newsletter h3{background:var(--green);color:var(--white);font-size:8px;font-weight:600;text-align:center;padding:4px 0}
.newsletter .field{margin:10px 10px 0;height:14px;border:1px solid var(--line);background:var(--white);font-size:6px;color:#aaa;padding:2px 4px}
.newsletter .subscribe{margin:12px 10px 0;height:14px;background:var(--green);color:var(--white);font-size:7px;text-align:center;line-height:14px}

/* footer */
.site-footer{position:absolute;top:1000px;left:0;width:714px;height:200px;background:var(--footer)}
.footer-top{position:absolute;top:12px;left:45px;right:45px;display:flex;gap:20px;font-size:6.5px;color:#aaa;border-bottom:1px solid #333;padding-bottom:8px}
.footer-brand{position:absolute;top:80px;left:282px;width:150px;height:30px;line-height:28px;border:1px solid #555;border-radius:15px;text-align:center;font-weight:700;font-size:14px;color:var(--white)}
.footer-line{position:absolute;top:95px;border-top:1px solid #444}
.footer-line.left{left:45px;width:225px}
.footer-line.right{left:444px;width:130px}
.social{position:absolute;top:89px;right:45px;display:flex;gap:5px}
.social span{width:12px;height:12px;border-radius:50%;background:#555}
.footer-bottom{position:absolute;bottom:0;left:0;width:714px;height:32px;background:var(--footer-deep);display:flex;align-items:center;padding:0 45px;gap:18px;font-size:6.5px;color:#999}
.footer-bottom .copy{margin-left:auto}
</style>
</head>
<body>

<header class="site-header">
  <div class="brand"><span class="dot"></span>Traineeway.Asia</div>
  <div class="top-tools">
    <span class="search">Search anything</span><span class="search-box"></span>
    <span class="btn-sm">Login</span><span class="btn-sm">Register</span>
  </div>
  <nav class="main-nav">
    <span>Home</span><span>Searching Jobs</span><span>Post Internship</span><span>User Profile</span><span>Featured Internship</span><span>Contact Us</span>
  </nav>
</header>

<div class="hero" role="img" aria-label="Photo of smiling university students studying together outdoors with books and a laptop"></div>

<section class="wrap welcome">
  <h1 class="section-title">Welcome to Traineeway.Asia</h1>
  <p>We link university and graduate students across Asia with meaningful internships at companies, startups and social ventures. Browse openings by country, field and duration, build a simple profile and apply in minutes. Employers post roles for free and reach motivated young talent ready to learn and contribute. Our team checks every listing so students can apply with confidence and grow real skills for their careers ahead. Explore featured roles below, read stories from past interns and sign up to receive new openings each week.</p>
</section>

<section class="wrap featured">
  <h2 class="center-title">Featured Jobs</h2>
  <div class="jobs">
    <article class="job"><div class="photo" role="img" aria-label="Photo of an intern at work"></div><p>Marketing intern wanted for a growing social startup in Singapore, three months.</p></article>
    <article class="job"><div class="photo" role="img" aria-label="Photo of an intern at work"></div><p>Research assistant role with an education nonprofit in Manila, flexible hours.</p></article>
    <article class="job"><div class="photo" role="img" aria-label="Photo of an intern at work"></div><p>Design intern to support a small studio in Kuala Lumpur on client work.</p></article>
    <article class="job"><div class="photo" role="img" aria-label="Photo of an intern at work"></div><p>Finance intern at a microcredit group in Jakarta, mentoring included.</p></article>
  </div>
</section>

<section class="testimonial">
  <h2>Testrimonial</h2>
  <svg class="quote-mark" width="24" height="24" viewBox="0 0 24 24" aria-hidden="true"><circle cx="12" cy="12" r="12" fill="#5a9e2a"/><text x="12" y="19" text-anchor="middle" font-family="Georgia,serif" font-size="16" fill="#fff">&#8220;</text></svg>
  <blockquote>My internship through this network opened doors I never expected. I worked on real projects, met mentors who cared about my growth and left with skills and confidence that helped me land my first full time role after graduation. I would recommend it to every student in the region looking for a start.</blockquote>
  <cite>Mei Tanaka</cite>
  <span class="role">Student</span>
</section>

<section class="wrap resources">
  <h2 class="section-title">Resources</h2>
  <div class="res-photo" role="img" aria-label="Photo of students reading together at a table"></div>
  <div class="res-text">
    <p>Guides and tips to help you prepare for your internship search. Learn how to write a clear resume, prepare for interviews and settle into a new city. Our resource library also covers visas, workplace culture across Asia and ways to make the most of each week on the job. New articles are added each month by our team and past interns sharing what they learned along the way.</p>
    <p style="margin-top:6px"><a>Read More »</a></p>
  </div>
  <aside class="newsletter">
    <h3>Newsletter Signup</h3>
    <div class="field">Enter Your Name</div>
    <div class="field">Enter Your Email</div>
    <div class="subscribe">Subscribe</div>
  </aside>
</section>

<footer class="site-footer">
  <div class="footer-top"><span>hello@traineeway.asia</span><span>+65 6000 0000</span></div>
  <span class="footer-line left"></span>
  <div class="footer-brand">Traineeway.Asia</div>
  <span class="footer-line right"></span>
  <div class="social"><span></span><span></span><span></span><span></span><span></span></div>
  <div class="footer-bottom">
    <span>Home</span><span>Search</span><span>Profile</span><span>Resources</span><span>Contact</span>
    <span class="copy">© 2024 Traineeway.Asia</span>
  </div>
</footer>

</body>
</html>
```